The Verdant Ledger App - Modernization & Graphics User Interface Friendliness Updates

We are Verdant Ledger, and we want to bring a new branding look and graphical user interface to the Verdant Ledger App. The app is a quick reference encyclopedia for all things produce. Boasting articles on over 2,000 produce items, with information ranging from taste and application to geographical and cultural significance. Included in its features are over 10 thousand recipes, and the Verdant Ledger App Harvest Circle – a global initiative to connect farmer, customer, and chef in one sustainable and easy to use application. The design needs to bring a greater sense of social connection – encouraging the user to participate in the 'Harvest Circled' experience voluntarily. The design should reflect a sense of authority reflecting the authenticity and reliability of the provided information, it's writing, and its sources. Download the App here: vledgr.example/install

Target Market(s)

Women and Men between ages 21-55.

Industry/Entity Type

Education

Font styles to use
Serif
Sans Serif

Colors

Designer to choose colors to be used in the design.

Requirements
Must have
• An updated user interface, the intuitive usability of the app is currently non-existent. We are looking to reflect as the authority on produce. The app design must reflect a professional, user-friendly, up-to-date, and trustworthy feel.
Nice to have
• To incorporate the social draw of the Harvest Circle we would like to include on the home page "Social Bubbles" (think Pictoloop stories) which updates with shared photos of produce and their location.
Should not have
• An overly complicated theme, distracting or unprofessional colors, and images.

```html
<!DOCTYPE html>
<html lang="en">
<head>
<meta charset="utf-8">
<title>User Profile – Verdant Ledger</title>
<link href="https://fonts.googleapis.com/css2?family=Raleway:wght@300;400;500;700;800&display=swap" rel="stylesheet">
<style>
:root{
  --screen:#fafafa;
  --ink:#1e1e1e;
  --muted:#6e6e6e;
  --faint:#b4b4b4;
  --icon:#c3c3c9;
  --card:#ffffff;
  --line:#ececec;
  --basil:#4f8a3a;
  --basil-dark:#2f5e22;
  --chile:#c8231c;
  --chile-dark:#7e1410;
  --greens:#6fa24b;
}
*{box-sizing:border-box;margin:0;padding:0}
html,body{width:769px;height:1200px;overflow:hidden}
body{background:var(--screen);font-family:"Raleway",sans-serif;color:var(--ink);position:relative}
.status-bar{position:absolute;top:0;left:0;width:100%;height:44px;display:flex;align-items:center;justify-content:space-between;padding:0 24px;font-size:21px;font-weight:500;font-family:"Helvetica Neue",Arial,sans-serif}
.status-left,.status-right{display:flex;align-items:center;gap:8px;width:230px}
.status-right{justify-content:flex-end}
.signal{display:flex;gap:3px}
.signal i{width:11px;height:11px;border-radius:50%;border:1.5px solid var(--ink);display:block}
.signal i.on{background:var(--ink)}
.battery{width:46px;height:19px;border:1.5px solid var(--ink);border-radius:4px;padding:2px;position:relative}
.battery::after{content:"";position:absolute;right:-5px;top:5px;width:3px;height:7px;background:var(--ink);border-radius:0 2px 2px 0}
.battery span{display:block;width:100%;height:100%;background:var(--ink);border-radius:2px}
.app-header{position:absolute;top:80px;left:0;width:100%;text-align:center}
.app-title{font-size:24px;font-weight:700}
.menu-button{position:absolute;right:46px;top:-4px;width:34px}
.menu-button span{display:block;height:4px;background:var(--ink);margin-bottom:6px;border-radius:1px}
.profile{position:absolute;top:152px;left:0;width:100%;text-align:center}
.avatar{width:222px;height:222px;margin:0 auto;border-radius:50%;border:8px solid #ececec;background:radial-gradient(circle at 50% 40%,#e7c0a5 0 32%,#c9867a 33% 60%,#6f8fb0 61%);}
.profile-name{margin-top:22px;font-size:37px;font-weight:800;letter-spacing:-.5px}
.profile-place{margin-top:12px;font-size:20px;font-weight:400;color:var(--muted)}
.stats{position:absolute;top:500px;left:95px;width:590px;display:flex;justify-content:space-between}
.stat{width:150px;text-align:center}
.stat-label{font-size:17px;font-weight:500}
.stat-value{margin-top:14px;font-size:42px;font-weight:300}
.stat-value small{font-size:22px}
.feed{position:absolute;top:633px;left:25px;width:719px;height:477px;overflow:hidden}
.card{position:absolute;width:352px;background:var(--card);box-shadow:0 1px 3px rgba(0,0,0,.08)}
.card-left{left:0;top:0}
.card-right{left:367px;top:0}
.card-third{left:367px;top:414px;height:80px}
.card-photo{display:block;width:100%}
.photo-basil{height:284px;background:linear-gradient(135deg,#7fb35a 0%,var(--basil) 45%,var(--basil-dark) 100%)}
.photo-chile{height:252px;background:radial-gradient(circle at 45% 55%,var(--chile) 0 48%,var(--chile-dark) 70%,#7a8c96 85%)}
.photo-greens{height:80px;background:linear-gradient(180deg,var(--greens),#3f6b2c)}
.card-body{padding:20px 24px 22px}
.card-title{font-size:18px;font-weight:700;text-transform:uppercase}
.card-source{margin-top:12px;font-size:16px;color:var(--muted);letter-spacing:.6px}
.card-note{margin-top:14px;font-size:11px;line-height:1.3;color:var(--faint)}
.card-author{margin-top:24px;display:flex;align-items:center;gap:14px;font-size:12px;color:var(--muted)}
.author-dot{width:26px;height:26px;border-radius:50%;background:#d9a896}
.tab-bar{position:absolute;bottom:0;left:0;width:100%;height:90px;background:var(--screen);border-top:1px solid var(--line);display:flex;justify-content:space-around;align-items:center;padding:0 40px}
.tab-bar svg{width:48px;height:48px;fill:var(--icon)}
</style>
</head>
<body>
<header class="status-bar">
  <div class="status-left">
    <div class="signal"><i class="on"></i><i class="on"></i><i class="on"></i><i></i><i></i></div>
    <span>NOVA</span>
    <svg width="22" height="16" viewBox="0 0 22 16"><path d="M11 15l3-3.5a4.5 4.5 0 0 0-6 0z" fill="#1e1e1e"/><path d="M4.5 8a9 9 0 0 1 13 0M1 4.5a14 14 0 0 1 20 0" stroke="#1e1e1e" stroke-width="2.2" fill="none" stroke-linecap="round"/></svg>
  </div>
  <span>4:21 PM</span>
  <div class="status-right">
    <svg width="12" height="20" viewBox="0 0 12 20"><path d="M1 5l10 10-5 4V1l5 4L1 15" stroke="#888" stroke-width="1.5" fill="none"/></svg>
    <span>100%</span>
    <div class="battery"><span></span></div>
  </div>
</header>

<div class="app-header">
  <h1 class="app-title">User Profile</h1>
  <div class="menu-button" aria-label="Menu"><span></span><span></span><span></span></div>
</div>

<section class="profile">
  <div class="avatar" role="img" aria-label="Profile photo of the user"></div>
  <h2 class="profile-name">Mateo Larkin</h2>
  <p class="profile-place">Los Angeles, California</p>
</section>

<section class="stats">
  <div class="stat"><p class="stat-label">Followers</p><p class="stat-value">2.2<small>k</small></p></div>
  <div class="stat"><p class="stat-label">Spotted</p><p class="stat-value">147</p></div>
  <div class="stat"><p class="stat-label">Recipes</p><p class="stat-value">6</p></div>
</section>

<section class="feed">
  <article class="card card-left">
    <div class="card-photo photo-basil" role="img" aria-label="Photo of fresh basil leaves"></div>
    <div class="card-body">
      <h3 class="card-title">Herbs Basil</h3>
      <p class="card-source">Bayline Growers Market</p>
      <p class="card-note">Fragrant sweet leaves picked this morning, best used fresh in sauces, salads and summer pesto.</p>
      <div class="card-author"><span class="author-dot"></span>Priya Halden</div>
    </div>
  </article>
  <article class="card card-right">
    <div class="card-photo photo-chile" role="img" aria-label="Photo of red chile peppers in a colander"></div>
    <div class="card-body">
      <h3 class="card-title">Pepper Chile de Agua</h3>
      <p class="card-source">Ridgeway Farms</p>
      <div class="card-author"><span class="author-dot"></span>Ines Barrow</div>
    </div>
  </article>
  <article class="card card-third">
    <div class="card-photo photo-greens" role="img" aria-label="Photo of leafy green herbs"></div>
  </article>
</section>

<nav class="tab-bar">
  <svg viewBox="0 0 48 48" aria-label="Produce"><path d="M24 14c-4-3-13-2-13 10 0 9 6 18 10 18 2 0 2-1 3-1s1 1 3 1c4 0 10-9 10-18 0-12-9-13-13-10z"/><path d="M24 13c0-5 3-8 7-9-1 5-3 8-7 9z"/></svg>
  <svg viewBox="0 0 48 48" aria-label="Recipes"><rect x="9" y="5" width="30" height="38" rx="1"/><path d="M17 14l14 16M31 14L17 30" stroke="#fafafa" stroke-width="3" stroke-linecap="round"/></svg>
  <svg viewBox="0 0 48 48" aria-label="Spotted"><path d="M2 24c6-9 14-14 22-14s16 5 22 14c-6 9-14 14-22 14S8 33 2 24z"/><circle cx="24" cy="24" r="9" fill="#fafafa"/><circle cx="24" cy="24" r="5"/></svg>
  <svg viewBox="0 0 48 48" aria-label="Gallery"><rect x="4" y="9" width="40" height="30"/><path d="M8 35l11-13 8 9 5-5 8 9z" fill="#fafafa"/><circle cx="34" cy="17" r="3" fill="#fafafa"/></svg>
  <svg viewBox="0 0 48 48" aria-label="Settings"><path d="M20 4h8l1 6 4 2 5-4 6 6-4 5 2 4 6 1v8l-6 1-2 4 4 5-6 6-5-4-4 2-1 6h-8l-1-6-4-2-5 4-6-6 4-5-2-4-6-1v-8l6-1 2-4-4-5 6-6 5 4 4-2z"/><circle cx="24" cy="24" r="6" fill="#fafafa"/></svg>
</nav>
</body>
</html>
```